Lumen Keyvault Password Manager WebApp Design

Lumen Keyvault is seeking an expert UI designer to provide a fresh and modern visual appeal for our product. Our inspiration comes from two major tools that have successfully managed to balance functionality and design aesthetics - Orbix Folder and Vaultmint. We want our application to exude a similar trustworthiness and modernity, through a clean, intuitive and responsive design.
We have established preliminary mockups and would like the designer to work within these parameters while enhancing the overall user experience. The primary tasks will involve innovative and improved designs of the login screen and the password screen, both being crucial touchpoints for our users. The login screen also serves a crucial role in demonstrating how our system works.
Key Elements:
Logo Integration: We are providing the logo for Lumen Keyvault. The design should align with the logo, both in terms of colors and overall aesthetic, to ensure a cohesive brand identity.
Color Palette: The UI design should adhere to the color palette derived from the logo to maintain brand consistency. The design should effectively utilize these colors to highlight important elements and improve user engagement.
Trustworthy and Modern Design: The UI should be professional and trustworthy. It should mirror the look and feel of Orbix Folder's simplicity and Vaultmint's solid security design, which inspires user confidence.
Adherence to Mockup Boundaries: The existing mockups serve as a guideline for the layout and placement of elements. The design should respect these boundaries while bringing innovation and visual appeal.
Improved Login Screen: The login screen is a key part of the user's journey and should be designed with utmost care. It should be intuitive, easy-to-use, visually engaging, and educative, showcasing how the system operates and encouraging users to sign in with confidence.
Enhanced Password Screen: The password screen, another key user touchpoint, needs improvement. The different types of passwords should be made more visible and intuitive, easing user interaction and enhancing the overall experience.
Prospective designers are encouraged to test our current version available for free at app.lumenkeyvault.com to understand the product better and contribute to meaningful design enhancements.
The goal of this project is to provide a visually compelling and user-friendly interface for Lumen Keyvault that inspires user trust, while adhering to the branding elements, including color scheme and logo design. The ideal designer will have a proven track record of creating compelling UI designs that enhance user experience and engagement.
We preferred the design to be in Figma.
Please provide the 3 design so we can evaluate if we like to choice you:
1. Login Page.
2. Passwords View design
3. Single Passwod Page
We need all the pages to be design that are provided as screenshots.

```html
<!DOCTYPE html>
<html lang="en">
<head>
<meta charset="utf-8">
<title>Lumen Keyvault – Login and Vault</title>
<link rel="stylesheet" href="https://fonts.googleapis.com/css2?family=Montserrat:wght@400;500;600;700&family=Lato:wght@400;700&display=swap">
<style>
:root{
  --page:#dcdcdc;
  --surface:#f8f8f8;
  --white:#ffffff;
  --green:#21a563;
  --green-bar:#31a763;
  --yellow:#ffd24d;
  --navy:#0a4aa6;
  --red:#ef5140;
  --blue:#3a67c4;
  --ink:#1c1c1c;
  --muted:#444;
  --line:#c9c9c9;
  --field:#f4f4f4;
}
*{box-sizing:border-box;margin:0;padding:0}
html,body{width:1012px;height:1200px;overflow:hidden}
body{background:var(--page);position:relative;font-family:"Lato",sans-serif;color:var(--ink)}
.abs{position:absolute}
.brand-stripe{position:absolute;left:0;top:0;width:100%;height:5px;background:linear-gradient(90deg,var(--green) 0 50%,var(--yellow) 50% 100%)}

/* Login screen */
.login{left:20px;top:26px;width:972px;height:546px;background:linear-gradient(135deg,#f1f1f1 0%,#fafafa 35%,#f4f4f4 60%,#fafafa 100%);overflow:hidden}
.login-brand{left:0;top:54px;width:100%;display:flex;justify-content:center;align-items:center;gap:18px}
.brand-square{width:30px;height:30px;background:var(--green);border-radius:3px}
.login-title{font-family:"Montserrat",sans-serif;font-weight:600;font-size:30px;letter-spacing:.5px;color:var(--ink)}
.feature-card{top:178px;width:273px;height:223px;background:var(--green);border-radius:9px;text-align:center;color:var(--white)}
.feature-card.lock{left:198px}
.feature-card.doc{left:514px}
.feature-icon{position:absolute;left:96px;top:30px;width:81px;height:81px;border-radius:50%;background:var(--yellow);border:11px solid var(--navy);display:flex;align-items:center;justify-content:center}
.feature-text{position:absolute;left:4px;right:4px;top:135px;font-family:"Montserrat",sans-serif;font-size:9.5px;line-height:18px;letter-spacing:-.1px}
.account-chooser{left:362px;top:440px;width:248px;height:46px;background:var(--white);border:1px solid #bdbdbd;border-radius:3px;padding:5px 0 0 10px}
.account-name{font-weight:700;font-size:13px;line-height:17px}
.account-mail{font-size:11px;color:var(--muted)}
.account-caret{position:absolute;right:42px;top:10px}
.account-badge{position:absolute;right:8px;top:8px;width:28px;height:28px;border-radius:50%;background:#e3e3e3}
.login-note{left:0;top:516px;width:100%;text-align:center;font-size:11.4px;color:var(--ink)}

/* Vault screen */
.vault{left:20px;top:604px;width:972px;height:546px;background:var(--white);overflow:hidden}
.sidebar{left:0;top:5px;width:215px;height:541px;background:var(--white);box-shadow:2px 0 4px rgba(0,0,0,.06)}
.side-brand{left:13px;top:8px;width:144px;height:35px;background:#f4f4f4;display:flex;align-items:center;gap:8px;padding-left:6px}
.side-brand .brand-square{width:20px;height:20px}
.side-brand span{font-family:"Montserrat",sans-serif;font-size:13px;color:#333}
.cat-head{left:0;top:83px;height:19px;border-left:3px solid var(--red);padding-left:13px;font-family:"Montserrat",sans-serif;font-weight:700;font-size:11.5px;color:var(--blue);line-height:19px}
.cat-list{left:16px;top:108px;list-style:none;width:190px}
.cat-list li{height:30.4px;display:flex;align-items:center;font-family:"Montserrat",sans-serif;font-size:9.4px;color:#333;position:relative}
.cat-list svg{width:10px;height:10px;margin-right:14px;flex:none;fill:var(--blue)}
.cat-list .chev{position:absolute;right:0;width:8px;height:8px;fill:none;stroke:#333;stroke-width:1.5}
.tabs{left:215px;top:5px;width:757px;height:43px;border-bottom:1px solid #eee;box-shadow:0 1px 2px rgba(0,0,0,.04)}
.tab{position:absolute;top:14px;display:flex;align-items:center;gap:6px;font-size:11px}
.tab.active{left:63px;height:29px;align-items:flex-start;border-bottom:3px solid var(--navy);padding-right:3px}
.tab svg{width:14px;height:14px;fill:#c7c7c7}
.tab.active svg{fill:var(--navy)}
.last-used{left:257px;top:67px;width:672px;height:39px;background:var(--green-bar);border-radius:6px;color:var(--white);font-size:17px;padding-left:12px;line-height:39px}
.last-used svg{position:absolute;right:10px;top:11px;width:17px;height:17px;fill:none;stroke:var(--white);stroke-width:2.6}
.entries{left:257px;top:118px;width:672px;display:grid;grid-template-columns:repeat(3,216px);column-gap:12px;row-gap:10.4px}
.entry{height:31px;background:var(--field);border:1px solid var(--line);border-radius:3px;display:flex;align-items:center;justify-content:space-between;padding:0 6px 0 8px;font-size:10px;color:#333}
.entry svg{width:11px;height:9px;fill:none;stroke:#222;stroke-width:1.3}
</style>
</head>
<body>
<svg width="0" height="0" style="position:absolute">
  <defs>
    <symbol id="card" viewBox="0 0 12 10"><rect x="0.7" y="0.7" width="10.6" height="8.6" rx="1"/><line x1="0.7" y1="3.5" x2="11.3" y2="3.5" stroke-width="1.6"/><line x1="2" y1="7" x2="5" y2="7"/></symbol>
    <symbol id="mail" viewBox="0 0 12 10"><rect x="0.7" y="0.7" width="10.6" height="8.6" rx="1"/><polyline points="0.7,1.2 6,5.5 11.3,1.2"/></symbol>
    <symbol id="money" viewBox="0 0 12 10"><rect x="0.7" y="1.2" width="10.6" height="7.6" rx="1" stroke-width="1.6"/><circle cx="6" cy="5" r="1.8"/></symbol>
  </defs>
</svg>

<section class="abs login">
  <div class="brand-stripe"></div>
  <div class="abs login-brand">
    <div class="brand-square"></div>
    <h1 class="login-title">LUMEN KEYVAULT</h1>
  </div>

  <article class="abs feature-card lock">
    <div class="feature-icon">
      <svg width="20" height="24" viewBox="0 0 20 24"><path d="M5 11V7a5 5 0 0 1 10 0v4" fill="none" stroke="#ef5140" stroke-width="2.6"/><rect x="1.5" y="10" width="17" height="13" rx="1.5" fill="#ef5140"/></svg>
    </div>
    <p class="feature-text">Lorem ipsum dolor sit amet, consectetur adipiscing<br>elit, sed do eiusmod tempor incididunt ut labore et<br>dolore magna aliqua. aliquip ex ea commodo</p>
  </article>

  <article class="abs feature-card doc">
    <div class="feature-icon">
      <svg width="26" height="32" viewBox="0 0 26 32"><path d="M1 1h16l8 8v22H1z" fill="#ef5140"/><path d="M17 1v8h8" fill="#ffb19f"/><g stroke="#ffd24d" stroke-width="2"><line x1="6" y1="16" x2="19" y2="16"/><line x1="6" y1="21" x2="19" y2="21"/><line x1="6" y1="26" x2="19" y2="26"/></g></svg>
    </div>
    <p class="feature-text">Lorem ipsum dolor sit amet, consectetur adipiscing<br>elit, sed do eiusmod tempor incididunt ut labore et<br>dolore magna aliqua. aliquip ex ea commodo</p>
  </article>

  <div class="abs account-chooser">
    <div class="account-name">Sign in as Pomelo</div>
    <div class="account-mail">pomelo.team@lumenkeyvault</div>
    <svg class="account-caret" width="8" height="6" viewBox="0 0 8 6"><polyline points="1,1 4,4 7,1" fill="none" stroke="#333" stroke-width="1.3"/></svg>
    <div class="account-badge"></div>
  </div>

  <p class="abs login-note">Nemo enim ipsam voluptatem quia voluptas sit aspernatur aut odit aut fugit, sed quia consequuntur magni dolores .</p>
</section>

<section class="abs vault">
  <div class="brand-stripe"></div>

  <aside class="abs sidebar">
    <div class="abs side-brand"><div class="brand-square"></div><span>Lumen Keyvault</span></div>
    <h2 class="abs cat-head">CATEGORIES</h2>
    <ul class="abs cat-list">
      <li><svg viewBox="0 0 10 10"><rect y="1" width="2" height="2"/><rect x="3" y="1" width="7" height="2"/><rect y="4" width="2" height="2"/><rect x="3" y="4" width="7" height="2"/><rect y="7" width="2" height="2"/><rect x="3" y="7" width="7" height="2"/></svg>General</li>
      <li><svg viewBox="0 0 10 10"><path d="M1.5 0h5l3 3v7h-8z"/></svg>Shared with me</li>
      <li><svg viewBox="0 0 10 10"><circle cx="5" cy="5" r="3.4"/><circle cx="5" cy="5" r="1.3" fill="#fff"/><rect x="4" y="0" width="2" height="10"/><rect x="0" y="4" width="10" height="2"/></svg>Work<svg class="chev" viewBox="0 0 8 8"><polyline points="1,2.5 4,5.5 7,2.5"/></svg></li>
      <li><svg viewBox="0 0 10 10"><circle cx="5" cy="3" r="2.4"/><path d="M0.8 10a4.2 4 0 0 1 8.4 0z"/></svg>Social media</li>
      <li><svg viewBox="0 0 10 10"><path d="M0 1h2l1.2 5h5.6L10 2.5H3"/><circle cx="3.8" cy="8.5" r="1"/><circle cx="8" cy="8.5" r="1"/></svg>Shopping</li>
      <li><svg viewBox="0 0 10 10"><rect x="0" y="2.5" width="10" height="7" rx="1"/><rect x="3.3" y="0.5" width="3.4" height="2.5" fill="none" stroke="#3a67c4"/></svg>Travel</li>
      <li><svg viewBox="0 0 10 10"><rect x="0.5" y="2" width="9" height="6" fill="none" stroke="#3a67c4"/><circle cx="5" cy="5" r="1.5"/></svg>$ Banking</li>
      <li><svg viewBox="0 0 10 10"><rect x="0.5" y="1.5" width="9" height="7" fill="none" stroke="#3a67c4"/><polyline points="0.5,2 5,5.5 9.5,2" fill="none" stroke="#3a67c4"/></svg>Emails</li>
      <li><svg viewBox="0 0 10 10"><rect x="4.2" y="1" width="1.6" height="8"/><path d="M2.5 2.5L5 0 7.5 2.5zM2.5 7.5L5 10 7.5 7.5z"/></svg>import-kVaultmint-08.02.23</li>
      <li><svg viewBox="0 0 10 10"><rect x="4.2" y="1" width="1.6" height="8"/><path d="M2.5 2.5L5 0 7.5 2.5zM2.5 7.5L5 10 7.5 7.5z"/></svg>11 import-kVaultmint-08.02.23</li>
      <li><svg viewBox="0 0 10 10"><rect x="4.2" y="1" width="1.6" height="8"/><path d="M2.5 2.5L5 0 7.5 2.5zM2.5 7.5L5 10 7.5 7.5z"/></svg>import-kVaultmint-08.02.23</li>
      <li><svg viewBox="0 0 10 10"><rect x="0" y="2.5" width="10" height="7" rx="1"/><rect x="3.3" y="0.5" width="3.4" height="2.5" fill="none" stroke="#3a67c4"/></svg>Testtt<svg class="chev" viewBox="0 0 8 8"><polyline points="1,2.5 4,5.5 7,2.5"/></svg></li>
      <li><svg viewBox="0 0 10 10"><rect x="0" y="2.5" width="10" height="7" rx="1"/><rect x="3.3" y="0.5" width="3.4" height="2.5" fill="none" stroke="#3a67c4"/></svg>Test 123</li>
      <li><svg viewBox="0 0 10 10"><rect x="0" y="2.5" width="10" height="7" rx="1"/><rect x="3.3" y="0.5" width="3.4" height="2.5" fill="none" stroke="#3a67c4"/></svg>Test 1213</li>
    </ul>
  </aside>

  <nav class="abs tabs">
    <div class="tab active"><svg viewBox="0 0 14 14"><path d="M7 1L0 7h2v6h4V9h2v4h4V7h2z"/></svg>Vault</div>
    <div class="tab" style="left:142px"><svg viewBox="0 0 14 14"><circle cx="7" cy="4" r="3.3"/><path d="M1 14a6 5.5 0 0 1 12 0z"/></svg></div>
    <div class="tab" style="left:197px"><svg viewBox="0 0 14 14"><path d="M7 1a4 4 0 0 0-4 4v4L1 11h12l-2-2V5a4 4 0 0 0-4-4z"/><circle cx="7" cy="12.5" r="1.5"/></svg></div>
    <div class="tab" style="left:252px"><svg viewBox="0 0 14 14"><rect y="2" width="14" height="1.6"/><rect y="5" width="14" height="1.6"/><rect y="8" width="14" height="1.6"/><rect y="11" width="14" height="1.6"/></svg></div>
  </nav>

  <div class="abs last-used">Last Used<svg viewBox="0 0 17 17"><circle cx="7" cy="7" r="5.2"/><line x1="11" y1="11" x2="15.5" y2="15.5"/></svg></div>

  <div class="abs entries">
    <div class="entry">Test 3333<svg><use href="#card"/></svg></div>
    <div class="entry">Test 1231<svg><use href="#card"/></svg></div>
    <div class="entry">Test 666<svg><use href="#card"/></svg></div>
    <div class="entry">Shopverra<svg><use href="#card"/></svg></div>
    <div class="entry">Wikiverse<svg><use href="#card"/></svg></div>
    <div class="entry">Cryptlock<svg><use href="#money"/></svg></div>
    <div class="entry">Chirpnet<svg><use href="#mail"/></svg></div>
    <div class="entry">kai@lumenkeyvault.com<svg><use href="#card"/></svg></div>
    <div class="entry">VQ<svg><use href="#card"/></svg></div>
    <div class="entry">Threadly<svg><use href="#card"/></svg></div>
    <div class="entry">Test ccc<svg><use href="#card"/></svg></div>
    <div class="entry">Test<svg><use href="#card"/></svg></div>
    <div class="entry">Filmdex<svg><use href="#card"/></svg></div>
    <div class="entry">Test 1111<svg><use href="#card"/></svg></div>
    <div class="entry">Test 77<svg><use href="#card"/></svg></div>
  </div>
</section>
</body>
</html>
```